new ownership of a business

Tax & accounting firm including payroll processing, business consulting, bookkeeping
I am a new owner and want to inform current clients I want the announcement to be subtle. something like "same friendly faces, brand new name" the name is going from "Wendell R. Pickett, CPA, PC" to "Pickett Marlowe & Associates, LLC" I would like to emphasize a little on the Marlowe part of the name. I would like the words "Tax Accountants" below the name.
Accounting

```html
<!DOCTYPE html>
<html lang="en">
<head>
<meta charset="utf-8">
<title>Pickett Marlowe &amp; Associates, LLC – Announcement Postcard</title>
<link rel="stylesheet" href="https://fonts.googleapis.com/css2?family=Cinzel:wght@400;500&family=Lato:wght@400;700&display=swap">
<style>
  :root {
    --page-bg: #ece8e2;
    --charcoal: #464646;
    --amber: #f0a830;
    --amber-deep: #ec9a22;
    --teal: #1a8aa6;
    --teal-light: #2ba3c0;
    --teal-dark: #0f6d86;
    --ink: #1f1f1f;
    --white: #ffffff;
    --photo-light: #efe9e2;
    --photo-mid: #c9b5a2;
  }
  html, body {
    margin: 0;
    padding: 0;
    width: 819px;
    height: 1200px;
    overflow: hidden;
    background: var(--page-bg);
  }
  .postcard {
    position: absolute;
    display: block;
    box-shadow: 0 2px 6px rgba(0,0,0,0.18);
  }
  .postcard--front { left: 72px; top: 52px; }
  .postcard--back  { left: 72px; top: 619px; }
  .display { font-family: "Cinzel", "Trajan Pro", serif; }
  .sans { font-family: "Lato", "Helvetica Neue", Arial, sans-serif; }
</style>
</head>
<body>

<!-- Front of postcard -->
<svg class="postcard postcard--front" width="685" height="530" viewBox="0 0 685 530" xmlns="http://www.w3.org/2000/svg">
  <defs>
    <linearGradient id="ribbonTeal" x1="0" y1="0" x2="1" y2="0">
      <stop offset="0" stop-color="var(--teal-dark)"/>
      <stop offset="0.5" stop-color="var(--teal-light)"/>
      <stop offset="1" stop-color="var(--teal)"/>
    </linearGradient>
    <linearGradient id="photoTone" x1="0" y1="0" x2="1" y2="1">
      <stop offset="0" stop-color="var(--photo-light)"/>
      <stop offset="1" stop-color="var(--photo-mid)"/>
    </linearGradient>
  </defs>

  <rect class="card-base" width="685" height="530" fill="var(--white)"/>
  <polygon class="band-charcoal" points="0,0 580,0 0,72" fill="var(--charcoal)"/>
  <polygon class="band-amber" points="0,72 580,0 685,0 685,192 0,300" fill="var(--amber)"/>
  <polygon class="photo-area" role="img" aria-label="Photo: silver piggy bank resting on a printed stock market chart"
           points="0,300 685,192 685,530 0,530" fill="url(#photoTone)"/>

  <polygon class="ribbon-fold" points="265,10 278,48 265,48" fill="var(--teal-dark)"/>
  <rect class="ribbon-headline" x="41" y="10" width="224" height="403" fill="url(#ribbonTeal)"/>

  <g class="headline display" fill="var(--white)" text-anchor="middle">
    <text x="154" y="146" font-size="21" letter-spacing="1">SAME FRIENDLY</text>
    <text x="154" y="198" font-size="52">FACES</text>
    <text x="154" y="251" font-size="24" letter-spacing="1">BRAND NEW</text>
    <text x="154" y="306" font-size="52">NAME</text>
  </g>

  <g class="firm-name" fill="var(--ink)" text-anchor="end">
    <text class="display" x="646" y="98" font-size="34">Pickett Marlowe</text>
    <text class="display" x="646" y="134" font-size="34">&amp; Associates, LLC</text>
    <line x1="305" y1="147" x2="646" y2="147" stroke="var(--ink)" stroke-width="2"/>
    <text class="sans" x="646" y="169" font-size="17">Tax Accountants</text>
  </g>
</svg>

<!-- Back of postcard -->
<svg class="postcard postcard--back" width="690" height="533" viewBox="0 0 690 533" xmlns="http://www.w3.org/2000/svg">
  <defs>
    <linearGradient id="backTeal" x1="0" y1="0" x2="1" y2="0">
      <stop offset="0" stop-color="var(--teal-dark)"/>
      <stop offset="0.55" stop-color="var(--teal-light)"/>
      <stop offset="1" stop-color="var(--teal)"/>
    </linearGradient>
  </defs>

  <rect class="card-base" width="690" height="533" fill="var(--white)"/>
  <polygon class="panel-amber" points="0,0 130,0 474,533 0,533" fill="var(--amber)"/>

  <polygon class="ribbon-about" points="0,62 244,18 244,96 0,156" fill="url(#backTeal)"/>
  <text class="display" x="26" y="100" font-size="31" font-weight="500" fill="var(--white)">About Us</text>

  <g class="about-copy sans" fill="var(--ink)" font-size="14">
    <text x="26" y="196">Lorem ipsum dolor sit amet,</text>
    <text x="26" y="214">consectetuer adipiscing elit,</text>
    <text x="26" y="232">sed diam nonummy nibh</text>
    <text x="26" y="250">euismod tincidunt ut laoreet</text>
    <text x="26" y="268">dolore magna aliquam erat volutpat.</text>
    <text x="26" y="286">Ut wisi enim ad minim veniam, quis</text>
    <text x="26" y="304">nostrud exerci tation ullamcorper</text>
    <text x="26" y="322">suscipit lobortis nisl ut aliquip ex ea</text>
    <text x="26" y="340">commodo consequat.</text>
  </g>

  <polygon class="ribbon-contact" points="0,411 426,353 426,456 0,516" fill="url(#backTeal)"/>
  <g class="contact sans" fill="var(--white)" font-size="15" font-weight="700">
    <path class="icon-pin" d="M33,420 a4.5,4.5 0 1 1 9,0 c0,3.5 -4.5,9 -4.5,9 s-4.5,-5.5 -4.5,-9z M37.5,418.2 a1.8,1.8 0 1 0 0.01,0z" fill="var(--white)" fill-rule="evenodd"/>
    <text x="44" y="431">42 Aspen Row St</text>
    <text x="44" y="451">Ridgway, CO 81432</text>
    <path class="icon-phone" d="M225,421 l3,-1 2,4 -2,1.5 c1,2 2,3 4,4 l1.5,-2 4,2 -1,3 c-6,0 -11.5,-5.5 -11.5,-11.5z" fill="var(--white)"/>
    <text x="238" y="431">970.555.0142</text>
    <rect class="icon-mail" x="224" y="443" width="11" height="8" fill="var(--white)"/>
    <polyline points="224,443 229.5,448 235,443" fill="none" stroke="var(--teal-dark)" stroke-width="1"/>
    <text x="238" y="451">info@pickettcpa.com</text>
  </g>

  <rect class="stamp-box" x="598" y="106" width="57" height="65" fill="none" stroke="var(--ink)" stroke-width="1.5"/>
  <g class="address-lines" stroke="var(--ink)" stroke-width="1.3">
    <line x1="452" y1="283" x2="656" y2="283"/>
    <line x1="452" y1="321" x2="656" y2="321"/>
    <line x1="452" y1="362" x2="656" y2="362"/>
  </g>
</svg>

</body>
</html>
```